BRINEWOOD PRODUCTIONS Video/Photo for Wedding/Events

We need a web design including the code which will be ready to launch. we are a Video and photography company in New Zealand and focus on medium to large Weddings and events.
The site will be our main point of contact with our customers with no more than 4-5 pages (Home, Pricing, Photo/Video Gallery, Contact) and we would like to be able to change the content of all pages as needed. The photos will be uploaded to our website but the videos we can only put the YouTube link.
I will add our company logo and some photos we have already taken to give you an idea of our product and services and can be used in the site as well.

Our pricing section will have photos, videos and photos + videos in 3 different pricing plans which we can upload and change as we need.

Here are some web pages to give you an idea of our industry and our competitors sites, however we would like the quality and design of our work to be better than all of our competitors sites which are listed below.

http://www.tallowpixel.example.nz/2012/02/9-great-new-zealand-photographers-websites/
http://rubquiphotography.example.uk/
http://www.doretavossphotography.example.nz/

Target Market(s)

our target audience is medium to up market customers who are looking at booking their wedding video/photography as well as events

Industry/Entity Type

Industry

Requirements
Must have
• The page must have a minimum of 4 pages, however we would like the designers to look outside the box and be creative with their designs.
Nice to have
• similar colors to our logo but don't limit your self and keep an open mind.

```html
<!DOCTYPE html>
<html lang="en">
<head>
<meta charset="utf-8">
<title>Brinewood Productions</title>
<link rel="stylesheet" href="https://fonts.googleapis.com/css2?family=Arimo:wght@400;700&family=Open+Sans:ital,wght@0,400;1,700&family=Lora:wght@400;700&family=Roboto+Condensed:wght@400&display=swap">
<style>
:root{
  --teal:#1a9aa6;
  --cyan:#19c3e0;
  --ink:#111;
  --text:#222;
  --grey:#666;
  --nav:#050505;
  --white:#fff;
}
*{margin:0;padding:0;box-sizing:border-box}
html,body{width:1200px;height:1125px;overflow:hidden;background:var(--white)}
body{position:relative;font-family:"Arimo",Arial,sans-serif;color:var(--text)}
.abs{position:absolute}

.brand{left:134px;top:40px;display:flex;align-items:center;gap:8px}
.brand-mark{width:14px;height:14px;border-radius:50%;background:var(--teal)}
.brand-name{font-family:"Arimo",Arial,sans-serif;font-size:19px;font-weight:400;color:var(--grey);letter-spacing:1px;line-height:1.2}

.social{right:64px;top:12px;display:flex;gap:12px}
.social span{width:16px;height:16px;border-radius:50%;background:#8a8a8a}

.call{right:120px;top:66px;display:flex;align-items:baseline;gap:8px}
.call-label{font-family:"Open Sans",sans-serif;font-style:italic;font-weight:700;font-size:32px;color:#333}
.call-number{font-family:"Open Sans",sans-serif;font-style:italic;font-weight:700;font-size:24px;color:var(--teal)}

.nav{left:0;top:136px;width:1200px;height:27px;background:linear-gradient(90deg,#bbb 0,#111 10%,var(--nav) 20%,var(--nav) 80%,#111 90%,#bbb 100%)}
.nav ul{list-style:none;display:flex;position:absolute;left:182px;top:0;height:27px}
.nav li{color:var(--white);font-size:15px;line-height:27px;padding:0 27px;border-left:1px solid #333}
.nav li:first-child{border-left:0;font-weight:700}

.slider{left:131px;top:173px;width:949px;height:366px;background:#3a3a3a;padding:7px;box-shadow:0 2px 6px rgba(0,0,0,.5)}
.slide{width:100%;height:100%;background:linear-gradient(100deg,#d9c9c4 0%,#8e6a7c 30%,#b78a8e 50%,#c8c9d8 70%,#9a9ab8 100%)}
.arrow{top:355px}

.welcome{left:136px;top:565px;width:670px}
.welcome h1{font-weight:400;font-size:24px;line-height:1.2;font-family:"Open Sans",sans-serif;color:var(--ink)}
.welcome h1 .name{font-family:"Lora",serif;font-size:30px;color:var(--teal)}
.welcome p{font-size:13.5px;line-height:19.2px;margin-top:4px;color:var(--text)}

.side-photo{left:816px;top:577px;width:255px;height:185px;background:var(--white);padding:5px;box-shadow:0 0 5px rgba(0,0,0,.35)}
.side-photo div{width:100%;height:100%;background:linear-gradient(160deg,#2c3a22 0%,#5a5a48 45%,#d9d7cf 75%,#8a8a70 100%)}

.divider{left:135px;top:773px;width:943px;border-top:1px dotted #333}

.card{top:792px;width:275px;height:157px;border-radius:10px;border:3px solid #666;background:linear-gradient(#222,#0c0c0c);color:var(--white);overflow:hidden}
.card .thumb{position:absolute;left:20px;top:2px;width:108px;height:85px}
.card h2{position:absolute;left:132px;top:4px;font-family:"Lora",serif;font-weight:700;font-size:21px;color:#eee;border-bottom:1px dotted #aaa;padding-bottom:2px;width:135px}
.card .lead,.card .rest{font-family:"Roboto Condensed","Arial Narrow",sans-serif;font-size:12.5px;line-height:17px;color:#ddd}
.card .lead{position:absolute;left:136px;top:37px;width:132px}
.card .rest{position:absolute;left:5px;top:91px;width:270px}
.card .more{position:absolute;right:18px;top:117px;width:70px;height:24px;border-radius:12px;border:2px solid #ccc;background:#111;font-family:"Roboto Condensed","Arial Narrow",sans-serif;font-size:12px;line-height:20px;text-align:center;color:var(--white)}

.footer{left:0;top:975px;width:1200px;height:150px;background:linear-gradient(90deg,#000 55%,#1a1a1a 80%,#0a0a0a 100%);border-top:4px solid var(--cyan)}
.footer ul{list-style:none;display:flex;position:absolute;left:137px;top:35px;font-size:13px;color:var(--white)}
.footer li+li::before{content:"|";padding:0 8px}
.footer li:first-child{font-weight:700}
</style>
</head>
<body>

<header>
  <div class="abs brand"><span class="brand-mark"></span><span class="brand-name">BRINEWOOD PRODUCTIONS</span></div>
  <div class="abs social" aria-label="Social links"><span></span><span></span><span></span><span></span></div>
  <div class="abs call"><span class="call-label">Call</span><span class="call-number">1.800.555.0142</span></div>
</header>

<nav class="abs nav">
  <ul><li>Home</li><li>Pricing</li><li>Photo Gallery</li><li>Video Gallery</li><li>Contact</li></ul>
</nav>

<section class="abs slider">
  <div class="slide" role="img" aria-label="Wedding photo: groom placing a ring on the bride's hand"></div>
</section>
<svg class="abs arrow" style="left:141px" width="16" height="28" viewBox="0 0 16 28"><path d="M16 0V28L0 14Z" fill="#111"/></svg>
<svg class="abs arrow" style="left:1053px" width="16" height="28" viewBox="0 0 16 28"><path d="M0 0V28L16 14Z" fill="#111"/></svg>

<section class="abs welcome">
  <h1>Welcome to <span class="name">BRINEWOOD</span></h1>
  <p>Lorem ipsum dolor sit amet, consectetur adipisicing elit, sed do eiusmod tempor incididunt ut labore et dolore magna aliqua. Ut enim ad minim veniam, quis nostrud exercitation ullamco laboris nisi ut aliquip ex ea commodo consequat. Duis aute irure dolor in reprehenderit in voluptate velit esse cillum dolore eu fugiat nulla pariatur. Excepteur sint occaecat cupidatat non proidentLorem ipsum dolor sit amet, consectetur adipisicing elit, sed do eiusmod tempor incididunt ut labore et dolore magna aliqua. Ut enim ad minim veniam, quis nostrud exercitation ullamco laboris nisi ut aliquip ex ea commodo consequat. Duis aute irure dolor in reprehenderit in voluptate velit esse cillum dolore eu fugiat nulla pariatur. Excepteur sint occaecat cupidatat non proident</p>
</section>
<div class="abs side-photo"><div role="img" aria-label="Photo of white ceremony chairs with flower arrangements"></div></div>

<div class="abs divider"></div>

<article class="abs card" style="left:137px">
  <div class="thumb" role="img" aria-label="Photo of a wedding couple" style="background:linear-gradient(135deg,#c89a6a,#e8d8c0)"></div>
  <h2>Lorem Ipsum</h2>
  <p class="lead">Lorem ipsum dolor sit amet, consectetur adipisicing elit, sed do</p>
  <p class="rest">adipisicing elit, sed do eiusmod termpo oincididu cididucididu</p>
  <span class="more">See More</span>
</article>
<article class="abs card" style="left:471px">
  <div class="thumb" role="img" aria-label="Photo of table flowers" style="background:linear-gradient(180deg,#4a5a30,#d8d070)"></div>
  <h2>Lorem Ipsum</h2>
  <p class="lead">Lorem ipsum dolor sit amet, consectetur adipisicing elit, sed do</p>
  <p class="rest">adipisicing elit, sed do eiusmod termpo oincididu cididucididu</p>
  <span class="more">See More</span>
</article>
<article class="abs card" style="left:803px">
  <div class="thumb" role="img" aria-label="Photo of ceremony chairs and flowers" style="background:linear-gradient(160deg,#2c3a22,#d9d7cf)"></div>
  <h2>Lorem Ipsum</h2>
  <p class="lead">Lorem ipsum dolor sit amet, consectetur adipisicing elit, sed do</p>
  <p class="rest">adipisicing elit, sed do eiusmod termpo oincididu cididucididu</p>
  <span class="more">See More</span>
</article>

<footer class="abs footer">
  <ul><li>Home</li><li>Pricing</li><li>Photo Gallery</li><li>Video Gallery</li><li>Contact</li></ul>
</footer>

</body>
</html>
```